Logo redesign & Stationery Design Project

We need a logo redesign for our company.

We also require the following stationary with the new logo:
*letterhead
*With compliments slips
*business card
*envelopes

We would like to maintain our current colours of navy blue and gold. We would like to maintain the wording on the back of our current business card.

Our existing letterhead and business card is attached.

Target Market(s)

Medical Professionals, Pharmacists, Lawyers

Industry/Entity Type

Business

Requirements
Must have
• See attached business card and letterhead, as all details on these documents need to be included.

```html
<!DOCTYPE html>
<html lang="en">
<head>
<meta charset="utf-8">
<title>Harrow Lane Financial Services – Letterhead</title>
<link href="https://fonts.googleapis.com/css2?family=PT+Sans:wght@400;700&family=Source+Sans+3:wght@300;400&display=swap" rel="stylesheet">
<style>
  :root {
    --navy: #1c3e6b;
    --gold: #9c8544;
    --ink: #333333;
    --muted: #7a7a7a;
    --backdrop: #e1e1e1;
    --paper: #ffffff;
  }
  * { margin: 0; padding: 0; box-sizing: border-box; }
  html, body { width: 1200px; height: 900px; overflow: hidden; }
  body { background: var(--backdrop); position: relative; font-family: "Source Sans 3", sans-serif; }

  .letterhead {
    position: absolute; left: 280px; top: 38px;
    width: 640px; height: 825px;
    background: var(--paper);
    overflow: hidden;
  }

  .brand {
    position: absolute; left: 38px; top: 76px;
    display: flex; align-items: center; gap: 8px;
    color: var(--navy);
    font-family: "Source Sans 3", sans-serif; font-weight: 400;
  }
  .brand-dot { width: 14px; height: 14px; border-radius: 50%; background: var(--navy); flex: none; }
  .brand-name { font-size: 17px; line-height: 18px; letter-spacing: 0.3px; }
  .brand-sub { display: block; font-size: 8px; line-height: 10px; letter-spacing: 2.6px; }

  .contact {
    position: absolute; top: 58px;
    font-size: 9.5px; line-height: 12.5px; font-weight: 300;
    color: var(--muted);
  }
  .contact .label { color: var(--gold); font-weight: 400; }
  .contact .web { color: var(--gold); font-weight: 400; }
  .contact-office { left: 300px; }
  .contact-postal { left: 451px; }

  .letter-body {
    position: absolute; left: 98px; top: 270px; width: 466px;
    font-family: "PT Sans", sans-serif; font-size: 10.4px; line-height: 12.4px;
    color: var(--ink); text-align: justify;
  }
  .letter-body p + p { margin-top: 12.4px; }

  .signature-area {
    position: absolute; left: 103px; top: 588px; width: 104px; height: 74px;
    background: linear-gradient(135deg, #f4f4f4, #e9e9e9);
  }

  .disclosure {
    position: absolute; left: 38px; top: 787px;
    font-size: 7px; color: var(--muted); font-weight: 300;
  }
  .rule-gold { position: absolute; left: 0; right: 0; top: 804px; height: 2px; background: var(--gold); }
  .band-navy { position: absolute; left: 0; right: 0; top: 808px; bottom: 0; background: var(--navy); }
</style>
</head>
<body>
  <main class="letterhead">
    <div class="brand">
      <span class="brand-dot"></span>
      <div class="brand-name">Harrow Lane<span class="brand-sub">Financial Services</span></div>
    </div>

    <address class="contact contact-office" style="font-style:normal">
      <span class="label">ABN</span> 51862304117<br>
      Suite 4, 118-120 Marlow Road<br>
      Elmstead NSW 2231
    </address>

    <address class="contact contact-postal" style="font-style:normal">
      PO BOX 4406 Ridgeway NSW 2231<br>
      <span class="label">T.</span> 02 9000 1120 &nbsp;<span class="label">F.</span> 02 9000 1124<br>
      <span class="label">E.</span> admin@harrowlane.com.au<br>
      <span class="web">www.harrowlane.com.au</span>
    </address>

    <section class="letter-body">
      <p>In dui turpis, varius vitae, tincidunt id, consequat ut, leo. Donec tincidunt tristique odio. Nulla erat felis, euismod nec, fringilla non, aliquet et, magna. Nulla at magna quis nisi pretium vehicula. Pellentesque habitant morbi tristique senectus et netus et malesuada fames ac turpis egestas. Class aptent taciti sociosqu ad litora torquent per conubia nostra, per inceptos himenaeos. In vel quam. Phasellus varius convallis purus. In non turpis. Nam sed risus. Etiam non neque at nisl gravida porttitor. Donec leo dolor, feugiat ut, pharetra et, porttitor a, metus. Suspendisse laoreet magna vel elit. Ut est augue, fermentum ac, molestie at, vestibulum et, urna.</p>
      <p>Nunc purus. Cras auctor. In ornare neque id ipsum. Nulla tincidunt, diam sit amet viverra euismod, sapien augue fringilla neque, at pellentesque felis tortor vel enim. Etiam dignissim. Sed a tortor vel nisl euismod ultricies. Donec molestie congue lectus. Integer sed turpis a tortor imperdiet consequat. Maecenas molestie placerat urna. Sed pede enim, sollicitudin nec, pretium nec, sollicitudin a, felis. In hac habitasse platea dictumst. Nam facilisis, tellus non scelerisque placerat, turpis turpis semper ante, euismod imperdiet augue nisi et neque. Vivamus tincidunt.</p>
      <p>Nulla lobortis ultricies nulla. Pellentesque purus mi, consequat quis, hendrerit sed, imperdiet non, eros. Nullam urna est, vehicula nec, cursus nec, dignissim sit amet, risus. Duis molestie, tellus sit amet laoreet ullamcorper, urna nisi fringilla ante, at rhoncus justo dolor vel dui. Nam hendrerit luctus lorem. Aenean tempor, metus vel posuere gravida, arcu nunc imperdiet tellus, ut blandit sem magna a turpis. Vivamus in neque. Lorem ipsum dolor sit amet, consectetuer adipiscing elit. Duis tristique tortor id nisl feugiat posuere. Maecenas posuere nisi ac risus. Nunc hendrerit. Praesent porta tempus ligula. Morbi in leo. Curabitur sapien nulla, cursus eget, faucibus in, porttitor et, odio. Praesent sed justo sed arcu commodo feugiat. Duis facilisis nulla ut eros. Cras libero. Donec mollis consectetuer metus. Praesent odio.</p>
    </section>

    <div class="signature-area" role="img" aria-label="Handwritten signature of the sender"></div>

    <p class="disclosure">Corporate Authorised Representative of Northgate Advice Group AFSL 400123</p>
    <div class="rule-gold"></div>
    <div class="band-navy"></div>
  </main>
</body>
</html>
```